we need PDF and print ready letterheads, dupplicated 5 times with different company details of different companies. All the companies are properties developments and no need for fancy logos (any reasonable shape is ok). Then simply change the companies details (names and company number) and the colour scheme slightly. I will supply the details.

The print ready should be 300dpi, and must have cropped marks.

Should be an easy job!

```html
<!DOCTYPE html>
<html lang="en">
<head>
<meta charset="utf-8">
<title>Letterhead</title>
<link href="https://fonts.googleapis.com/css2?family=Jost:wght@500&family=Montserrat:wght@400;600&family=Open+Sans:wght@300;400;600&display=swap" rel="stylesheet">
<style>
  :root {
    --ink-dark: #1b1b1c;
    --accent-red: #b80000;
    --brand-blue: #1e90ff;
    --heading: #2b3136;
    --body: #4a4f55;
    --paper: #ffffff;
    --crop-mark: #ffffff;
  }
  html, body { margin: 0; padding: 0; overflow: hidden; }
  body { width: 927px; height: 1200px; background: var(--paper); }
  .letterhead {
    position: relative; width: 927px; height: 1200px; overflow: hidden;
    background: var(--paper); font-family: "Open Sans", sans-serif; color: var(--body);
  }
  .header-shape { position: absolute; left: 0; top: 0; }
  .brand { position: absolute; left: 90px; top: 206px; width: 222px; text-align: center; }
  .brand-square { width: 44px; height: 44px; border: 4px solid var(--brand-blue); box-sizing: border-box; margin: 0 auto 14px; }
  .brand-name { font-weight: 600; font-size: 27px; color: var(--heading); letter-spacing: 0.3px; line-height: 1; white-space: nowrap; }
  .content { position: absolute; left: 120px; top: 398px; width: 700px; }
  .headline { font-family: "Jost", sans-serif; font-weight: 500; font-size: 50px; color: var(--heading); margin: 0 0 14px; line-height: 1.1; }
  .subhead { font-family: "Jost", sans-serif; font-weight: 500; font-size: 30px; color: var(--heading); margin: 40px 0 24px; line-height: 1.2; }
  .para { margin: 0; white-space: nowrap; font-weight: 400; }
  .para-intro { font-size: 19.4px; line-height: 23.6px; }
  .para-main { font-size: 20.8px; line-height: 25.6px; margin-top: 36px; }
  .para-subhead { font-size: 20.8px; line-height: 25.6px; }
  .sign-off { position: absolute; left: 122px; top: 995px; font-size: 17.6px; }
  .sign-off p { margin: 0; }
  .signature-area { width: 188px; height: 66px; margin: 6px 0 6px -2px; border-radius: 4px;
    background: linear-gradient(90deg, #e4e5e7, #f2f3f4); }
  .contact-person { position: absolute; right: 103px; top: 958px; text-align: right; }
  .person-name { font-family: "Montserrat", sans-serif; font-weight: 600; font-size: 36px; color: var(--ink-dark); margin: 0; line-height: 1.1; }
  .person-role { font-family: "Montserrat", sans-serif; font-weight: 400; font-size: 20px; letter-spacing: 1px; color: #333; margin: 0; line-height: 1.2; }
  .address { position: absolute; right: 91px; top: 1050px; display: flex; align-items: center; gap: 10px; font-size: 24px; color: var(--ink-dark); }
  .footer { position: absolute; left: 0; bottom: 0; width: 927px; height: 56px; background: var(--ink-dark);
    display: flex; align-items: center; justify-content: center; gap: 14px; color: #fff; font-size: 20px; }
  .footer-item { display: flex; align-items: center; gap: 12px; }
  .footer svg { display: block; }
  .crop-marks { position: absolute; left: 0; top: 0; pointer-events: none; }
</style>
</head>
<body>
<div class="letterhead">
  <svg class="header-shape" width="927" height="220" viewBox="0 0 927 220" aria-hidden="true">
    <polygon points="0,0 927,0 927,188 731,80 588,144 390,82 0,202" fill="var(--ink-dark)"/>
    <polyline points="0,202 390,82 756,202" fill="none" stroke="var(--accent-red)" stroke-width="11"/>
    <polyline points="588,144 731,80 927,188" fill="none" stroke="var(--accent-red)" stroke-width="11"/>
  </svg>

  <div class="brand">
    <div class="brand-square"></div>
    <div class="brand-name">COMPANY NAME</div>
  </div>

  <main class="content">
    <h1 class="headline">HEADLINE</h1>
    <p class="para para-intro">Lorem ipsum dolor sit amet, consectetuer adipiscing elit, sed diam nonummy<br>nibh euismod tincidunt ut laoreet dolore magna aliquam erat volutpat. Ut wisi<br>enim ad minim veniam, quis nostrud exerci tation ullamcorper suscipit lobor-<br>tis nisl ut aliquip ex ea commodo consequat. Duis autem vel eum iriure dolor<br>in hendrerit in vulputate velit esse molestie consequat, vel illum dolore eu</p>
    <p class="para para-main">Lorem ipsum dolor sit amet, consectetuer adipiscing elit, sed diam<br>nonummy nibh euismod tincidunt ut laoreet dolore magna aliquam erat</p>
    <h2 class="subhead">PLACE YOUR TEXT HERE</h2>
    <p class="para para-subhead">Lorem ipsum dolor sit amet, consectetuer adipiscing elit, sed diam<br>nonummy nibh euismod tincidunt ut laoreet dolore magna aliquam erat<br>volutpat. Ut wisi enim ad minim veniam, quis nostrud exerci tation<br>ullamcorper suscipit lobortis nisl ut aliquip ex ea commodo consequat.<br>Duis autem vel eum iriure dolor in hendrerit in vulputate velit esse mo-<br>lestie consequat, vel illum dolore eu feugiat nulla facilisis at vero eros et</p>
  </main>

  <div class="sign-off">
    <p>Regard</p>
    <div class="signature-area" role="img" aria-label="Handwritten signature of the art director"></div>
    <p>Art Director</p>
  </div>

  <div class="contact-person">
    <p class="person-name">Alden Pryce</p>
    <p class="person-role">Managing Member</p>
  </div>

  <div class="address">
    <span>your address here</span>
    <svg width="26" height="34" viewBox="0 0 26 34" aria-hidden="true">
      <path d="M13 0C5.8 0 0 5.6 0 12.6 0 22 13 34 13 34s13-12 13-21.4C26 5.6 20.2 0 13 0z" fill="var(--ink-dark)"/>
      <circle cx="13" cy="12.5" r="5" fill="#fff"/>
    </svg>
  </div>

  <footer class="footer">
    <span class="footer-item">www.northgate-homes.com
      <svg width="18" height="18" viewBox="0 0 18 18" aria-hidden="true" fill="none" stroke="#fff" stroke-width="1.4">
        <circle cx="9" cy="9" r="7.5"/><ellipse cx="9" cy="9" rx="3.3" ry="7.5"/><line x1="1.5" y1="9" x2="16.5" y2="9"/><line x1="3" y1="5" x2="15" y2="5"/><line x1="3" y1="13" x2="15" y2="13"/>
      </svg>
    </span>
    <span class="footer-item">@northgate-homes.com
      <svg width="20" height="14" viewBox="0 0 20 14" aria-hidden="true">
        <rect x="0" y="0" width="20" height="14" fill="#fff"/><polyline points="0,0 10,8 20,0" fill="none" stroke="var(--ink-dark)" stroke-width="1.6"/>
      </svg>
    </span>
    <span class="footer-item">0312-555-014
      <svg width="20" height="20" viewBox="0 0 20 20" aria-hidden="true">
        <path d="M4 2l3 0 1.5 4-2 1.5c1 2.2 2.8 4 5 5L13 10.5l4 1.5v3c0 1-1 2-2 2C8.4 17 3 11.6 3 5c0-1 0-3 1-3z" fill="#fff"/>
      </svg>
    </span>
  </footer>

  <svg class="crop-marks" width="927" height="1200" viewBox="0 0 927 1200" aria-hidden="true" stroke="var(--crop-mark)" stroke-width="0.8">
    <line x1="0" y1="11" x2="7" y2="11"/><line x1="11" y1="0" x2="11" y2="7"/>
    <line x1="920" y1="11" x2="927" y2="11"/><line x1="916" y1="0" x2="916" y2="7"/>
    <line x1="0" y1="1189" x2="7" y2="1189"/><line x1="11" y1="1193" x2="11" y2="1200"/>
    <line x1="920" y1="1189" x2="927" y2="1189"/><line x1="916" y1="1193" x2="916" y2="1200"/>
  </svg>
</div>
</body>
</html>
```